vehicle livery flyer

a flyer to go under windscreen wipers solely aimed at van drivers / companies using the vans for advertising thier companies.... ie Van Livery

use company logo , file supplied and be creative

id like this re designed, using different pictures , same logo....in a postcard style.

Livery

```html
<!DOCTYPE html>
<html lang="en">
<head>
<meta charset="utf-8">
<title>KVT Print – Vehicle Livery Flyers</title>
<link rel="stylesheet" href="https://fonts.googleapis.com/css2?family=Archivo+Black&family=Arimo:wght@400;700&display=swap">
<style>
  :root {
    --canvas: #ffffff;
    --paper: #f8f8f8;
    --paper-edge: #e4e4e4;
    --ink: #1c1c1c;
    --pink: #e5197e;
    --plum: #a3335f;
    --brown: #7a4a36;
    --teal: #17806d;
    --blue: #3aa9e0;
    --sky: #7cc4e6;
    --green: #6fb846;
    --lime: #a8d05a;
    --rule: #222222;
  }
  * { box-sizing: border-box; margin: 0; padding: 0; }
  html, body { width: 1200px; height: 1000px; overflow: hidden; background: var(--canvas); }
  body { position: relative; font-family: "Arimo", Arial, sans-serif; color: var(--ink); }

  .flyer {
    position: absolute;
    width: 472px;
    height: 666px;
    background: var(--paper);
    border: 1px solid var(--paper-edge);
    overflow: hidden;
  }
  .flyer--intro { left: 115px; top: 218px; }
  .flyer--vehicles { left: 629px; top: 100px; }

  .header-band { position: absolute; left: 0; top: 0; width: 472px; height: 62px; display: block; }

  .headline {
    position: absolute;
    left: 0; width: 100%;
    text-align: center;
    font-family: "Archivo Black", "Arial Black", sans-serif;
    text-transform: uppercase;
    line-height: 1;
    background: linear-gradient(90deg, var(--pink) 0%, var(--brown) 22%, var(--teal) 45%, var(--blue) 68%, var(--green) 100%);
    -webkit-background-clip: text;
    background-clip: text;
    color: transparent;
  }
  .headline--hello { top: 90px; font-size: 38px; letter-spacing: 1px; }
  .headline--vehicle { top: 80px; font-size: 46px; letter-spacing: 1px; line-height: 38px; }

  .body-copy {
    position: absolute;
    font-size: 9.6px;
    line-height: 11.6px;
    text-align: center;
  }
  .body-copy p { margin-bottom: 11.6px; }
  .body-copy strong { font-weight: 700; }
  .flyer--intro .body-copy { left: 54px; width: 364px; top: 145px; }
  .flyer--vehicles .body-copy { left: 66px; width: 340px; top: 168px; }

  .brand-mark {
    position: absolute;
    left: 180px; top: 486px;
    display: flex; align-items: center; gap: 10px;
  }
  .brand-mark__dot { width: 40px; height: 40px; border-radius: 50%; background: var(--blue); }
  .brand-mark__name { font-family: "Arimo", Arial, sans-serif; font-weight: 700; font-size: 26px; color: var(--teal); }

  .photo-grid {
    position: absolute;
    left: 69px; top: 346px;
    display: grid;
    grid-template-columns: 144px 187px;
    grid-template-rows: 107px 99px;
    gap: 7px 6px;
  }
  .photo { display: block; width: 100%; height: 100%; }
  .photo--red-van { background: linear-gradient(135deg, #7b8a5a, #c8252b 55%, #8e1c22); }
  .photo--green-car { background: linear-gradient(135deg, #8f9a9a, #8dc43f 50%, #dfe8d0); }
  .photo--blue-van { background: linear-gradient(135deg, #c9b27a, #1e3a78 50%, #e07a1f); }
  .photo--white-van { background: linear-gradient(135deg, #6f7a5c, #e9edf0 45%, #2f8fd0); }

  .contact {
    position: absolute;
    left: 50px; width: 372px;
    text-align: center;
    font-size: 9.8px;
    line-height: 12px;
  }
  .contact__rule { border-top: 1px solid var(--rule); margin-bottom: 8px; }
  .contact__title { font-weight: 700; margin-bottom: 3px; }
  .flyer--intro .contact { top: 601px; }
  .flyer--vehicles .contact { top: 600px; }
</style>
</head>
<body>

<svg width="0" height="0" style="position:absolute" aria-hidden="true">
  <defs>
    <linearGradient id="band-gradient" x1="0" y1="0" x2="1" y2="0">
      <stop offset="0" stop-color="#e5197e"/>
      <stop offset="0.2" stop-color="#a3335f"/>
      <stop offset="0.38" stop-color="#7a4a36"/>
      <stop offset="0.55" stop-color="#17806d"/>
      <stop offset="0.72" stop-color="#3aa9e0"/>
      <stop offset="0.86" stop-color="#7cc4e6"/>
      <stop offset="1" stop-color="#a8d05a"/>
    </linearGradient>
  </defs>
</svg>

<!-- Intro flyer -->
<section class="flyer flyer--intro">
  <svg class="header-band" viewBox="0 0 472 62" aria-hidden="true">
    <path d="M0 0 H472 V60 C330 32 150 34 0 54 Z" fill="url(#band-gradient)"/>
  </svg>

  <h1 class="headline headline--hello">Hello!</h1>

  <div class="body-copy">
    <p>We are a printing company with over 50 years experience in <strong>Screen print</strong> and over 10 years experience in <strong>Digital print</strong> so there is no better place to visit then KVT.</p>
    <p>As a well established printing business we are able to offer you help and advice from the design stage all the way though to installation. Through our many years of experience we have produced works for some of the biggest names in Banking, Fashion and Music.</p>
    <p>KVT moved into digital printing over 10 years ago, with our policy of making sure <strong>quality</strong> is at the forefront of our aim. In its simplest form, Digital print is <strong>low-cost</strong> with a lower environmental impact compared to screen printing which enables us to pass savings on to our customers. So if you are looking for a one off show card to multiple run large signage, KVT can meet all of your needs.</p>
    <p>KVT can also offer traditional screen printing onto a <strong>wide range of materials</strong>. Our expertise in printing difficult substrate such as corrugated boards, uncoated boards and papers, display boards, plastics, metals and glass, we also do the run of the mill self cling/self adhesive, rigid pvc's. With the ability to handle runs into the 1000's KVT will deliver first class results, on time and on budget.</p>
    <p>Located in Brookfield, Kent, the company is well able to meet the most exacting demands of its customers and yet, is still able to offer that all important personal touch, coupled with quality design and reliability.</p>
  </div>

  <div class="brand-mark">
    <span class="brand-mark__dot"></span>
    <span class="brand-mark__name">KVT Print</span>
  </div>

  <footer class="contact">
    <div class="contact__rule"></div>
    <p class="contact__title">For further information on our vehicle graphics:</p>
    <p>020 7946 0321 &nbsp;|&nbsp; hello@kvt-print.com</p>
    <p>18 Alder Row, Brookfield, Kent, BF2 7QJ</p>
  </footer>
</section>

<!-- Vehicle graphics flyer -->
<section class="flyer flyer--vehicles">
  <svg class="header-band" viewBox="0 0 472 62" aria-hidden="true">
    <path d="M0 0 H472 V60 C330 32 150 34 0 54 Z" fill="url(#band-gradient)"/>
  </svg>

  <h1 class="headline headline--vehicle">Vehicle<br>Graphics</h1>

  <div class="body-copy">
    <p><strong>Vehicle graphics</strong> are one of the most <strong>cost-effective</strong> ways to raise the profile of your business and how it's seen. From simple logos and contact details to bright colourful vehicle wraps, KVT can turn your car, sports car, taxi, van, truck or bus into a mobile advertising board.</p>
    <p>So if you are looking for car graphics, vehicle wrapping, signwriting, custom decals, lorry &amp; bus graphic, fleet graphics &amp; promotional vinyl graphics KVT can help.</p>
    <p>Don't lose the marketing opportunity, display your brand and services to the masses. KVT are Specialists in commercial fleet livery so whether it be 1 or 100 vehicles, KVT leads the field by creating high quality graphics on time and to your budget.</p>
  </div>

  <div class="photo-grid">
    <div class="photo photo--red-van" role="img" aria-label="Photo of a red van wrapped in coffee-brand livery"></div>
    <div class="photo photo--green-car" role="img" aria-label="Photo of a small car in a full green and white promotional wrap"></div>
    <div class="photo photo--blue-van" role="img" aria-label="Photo of a navy van with orange chevron fleet graphics"></div>
    <div class="photo photo--white-van" role="img" aria-label="Photo of a white van with blue and yellow circular livery"></div>
  </div>

  <footer class="contact">
    <div class="contact__rule"></div>
    <p class="contact__title">For further information on our vehicle graphics:</p>
    <p>020 7946 0321 &nbsp;|&nbsp; hello@kvt-print.com</p>
    <p>18 Alder Row, Brookfield, Kent, BF2 7QJ</p>
  </footer>
</section>

</body>
</html>
```